Personal Injury Mailer for a Chiropractic Office

I need a postcard design for our new Chiropractic office called "Varden Chiropractic". I am looking to treat more traumatic injuries such as those caused by auto accidents. I treat using gentle Chiropractic care in combination with Deep Mobility Protocol soft tissue massage.

I like some of the elements of the uploaded .jpgs: the smashed car on the one and the lady rubbing her neck and back on the other. I DO NOT like the soft collar neck brace. I would rather the person in the picture be female than male. I am only mailing to potential clients who are not at fault, so I want to communicate to them that their treatment will, in all probability, be at no cost to them. I like the message on the "If you've been in an auto accident, the real damage may not be this obvious" or something to that effect. So many people neglect to get proper treatment after an accident and the effects of these injuries show up down the road.

Please include my headshot (not prominently). Please include "Let us review your case. Schedule a Consult today and receive a FREE tube of Glacimint Pain Reliever ($10 value)." [$10 value in small print] The phrases: "This is an advertisement for chiropractic services." and "If you decide to purchase additional treatment, you have the legal right to change your mind within three days and receive a refund." must be included as disclaimers in small print. They can be place on the address side of the postcard.

I have also included my logo in a few different formats and 3 versions of the DMP/Tidewalker logo.
(555) 308-4176
www.vardenchiro.com

```html
<!DOCTYPE html>
<html lang="en">
<head>
<meta charset="utf-8">
<title>Varden Chiropractic – Auto Accident Postcard</title>
<link href="https://fonts.googleapis.com/css2?family=Ubuntu:wght@500&family=PT+Sans:wght@400;700&family=Cinzel:wght@500&display=swap" rel="stylesheet">
<style>
  :root {
    --backdrop: #d9742a;
    --card: #ffffff;
    --cyan: #1fb4e6;
    --navy: #0d2f7a;
    --blue: #1a6fc9;
    --sky: #7fd0f2;
    --red: #e3232c;
    --ink: #1d1d1d;
    --photo-a: #c9ccd3;
    --photo-b: #e9b7c8;
  }
  * { box-sizing: border-box; margin: 0; padding: 0; }
  html, body { width: 1200px; height: 784px; overflow: hidden; background: var(--backdrop); }
  .postcard {
    position: absolute; left: 20px; top: 20px; width: 1160px; height: 744px;
    background: var(--card); overflow: hidden;
    font-family: "PT Sans", sans-serif; color: var(--ink);
  }
  .scene-photo {
    position: absolute; left: 0; top: 182px; width: 484px; height: 410px;
    background: linear-gradient(120deg, var(--photo-a) 0%, #b9bdc6 45%, var(--photo-b) 75%, #f3d6c4 100%);
  }
  .waves { position: absolute; inset: 0; }
  .headline {
    position: absolute; right: 480px; top: 64px;
    font-family: "Ubuntu", sans-serif; font-weight: 500; font-size: 24px; line-height: 34px;
    color: var(--cyan); text-align: right; white-space: nowrap;
  }
  .brand {
    position: absolute; left: 762px; top: 78px;
    display: flex; align-items: center; gap: 12px; white-space: nowrap;
    font-family: "Cinzel", serif; font-size: 27px; color: var(--navy); letter-spacing: 0.5px;
  }
  .brand-dot { width: 20px; height: 20px; border-radius: 50%; background: var(--blue); }
  .offer {
    position: absolute; right: 38px; top: 226px;
    font-size: 37px; line-height: 57px; text-align: right; color: var(--ink); white-space: nowrap;
  }
  .offer small { font-size: 21px; }
  .disclaimers {
    position: absolute; right: 40px; top: 552px; width: 290px;
    font-size: 14px; line-height: 19px; text-align: right; color: var(--ink);
  }
  .partners {
    position: absolute; left: 24px; top: 680px; height: 48px; display: flex; align-items: center;
  }
  .partner-name { display: flex; align-items: center; gap: 8px; font-size: 34px; font-weight: 700; color: var(--red); }
  .partner-name .mark { width: 14px; height: 14px; border-radius: 50%; background: var(--red); }
  .divider { width: 1px; height: 54px; background: #8aa0c0; margin: 0 28px 0 44px; }
  .badge { width: 166px; height: 42px; background: var(--navy); border-radius: 3px; }
  .contact {
    position: absolute; left: 466px; top: 674px; font-size: 22px; line-height: 32px; color: var(--ink);
  }
  .contact div { display: flex; align-items: center; gap: 8px; white-space: nowrap; }
</style>
</head>
<body>
<main class="postcard">
  <div class="scene-photo" role="img" aria-label="Photo of a damaged silver car with deployed airbag and a woman in a pink top holding her sore neck"></div>

  <svg class="waves" viewBox="0 0 1160 744" aria-hidden="true">
    <path d="M0 556 Q600 565 1160 462 L1160 478 Q600 582 0 572 Z" fill="var(--sky)"/>
    <path d="M0 580 Q620 595 1160 486 L1160 540 Q650 640 0 622 Z" fill="var(--blue)"/>
    <path d="M720 744 Q960 725 1160 690 L1160 716 Q1040 740 960 744 Z" fill="var(--red)"/>
  </svg>

  <p class="headline">"If You've been in An Auto Accident,<br>The Real Damage May Not Be This Obvious"</p>

  <div class="brand"><span class="brand-dot"></span>Varden Chiropractic</div>

  <p class="offer">"Let us Review your case.<br>Schedule a Consult Today<br>and Receive a FREE tube of<br>Glacimint Pain Reliever <small>($10 value)</small>"</p>

  <p class="disclaimers">Disclaimers:<br>"This is an advertisement for chiropractic services." and "If you decide to purchase additional treatment, you have the legal right to change your mind within three days and receive a refund."</p>

  <div class="partners">
    <div class="partner-name"><span class="mark"></span>DMP</div>
    <div class="divider"></div>
    <div class="badge" role="img" aria-label="Tidewalker partner badge"></div>
  </div>

  <div class="contact">
    <div>
      <svg width="20" height="20" viewBox="0 0 20 20" aria-hidden="true"><circle cx="10" cy="10" r="9" fill="none" stroke="currentColor" stroke-width="1.5"/><path d="M7 5 L9 8 L8 9 Q9 11 11 12 L12 11 L15 13 L14 15 Q9 15 5 7 Z" fill="currentColor"/></svg>
      (555) 308-4176
    </div>
    <div>
      <svg width="18" height="18" viewBox="0 0 20 20" aria-hidden="true"><circle cx="10" cy="10" r="8.5" fill="none" stroke="currentColor" stroke-width="1.5"/><path d="M1.5 10 H18.5 M10 1.5 Q5 10 10 18.5 M10 1.5 Q15 10 10 18.5" fill="none" stroke="currentColor" stroke-width="1.3"/></svg>
      www.vardenchiro.com
    </div>
  </div>
</main>
</body>
</html>
```